Card Layout for my Industrial Coating (Paint) company
Coatings Company Business Card Layout
Professional
Marcus D. Alvord
President / Owner
712 Tamber Rd. Brennick, WI 54000
malvord@lumorafinishworks.com

```html
<!DOCTYPE html>
<html lang="en">
<head>
<meta charset="utf-8">
<title>Lumora Finish Works – Business Card</title>
<link href="https://fonts.googleapis.com/css2?family=Josefin+Sans:wght@400;600&display=swap" rel="stylesheet">
<style>
  :root {
    --page-bg: #e9e7e4;
    --card-white: #ffffff;
    --brand-maroon: #8e2b31;
    --swoosh-light: #d9d9d9;
    --swoosh-dark: #8c8c8c;
    --ink-light: #ffffff;
  }
  html, body {
    margin: 0;
    padding: 0;
    width: 1200px;
    height: 914px;
    overflow: hidden;
    background: var(--page-bg);
    font-family: "Josefin Sans", sans-serif;
  }
  .card {
    position: absolute;
    left: 100px;
    top: 171px;
    width: 1000px;
    height: 571px;
    background: var(--card-white);
    box-shadow: 0 10px 30px rgba(0,0,0,0.18);
    overflow: hidden;
  }
  .card-art {
    position: absolute;
    inset: 0;
  }
  .holder {
    position: absolute;
    left: 52px;
    top: 46px;
    color: var(--ink-light);
    font-variant: small-caps;
    letter-spacing: 0.14em;
  }
  .holder-name {
    font-size: 26px;
    font-weight: 600;
    margin: 0 0 8px;
  }
  .holder-title {
    font-size: 20px;
    margin: 0;
  }
  .contact {
    position: absolute;
    left: 52px;
    bottom: 64px;
    margin: 0;
    padding: 0;
    list-style: none;
    color: var(--ink-light);
    font-size: 13px;
    letter-spacing: 0.08em;
    text-transform: uppercase;
  }
  .contact li {
    display: flex;
    align-items: center;
    gap: 10px;
    height: 22px;
  }
  .contact-icon {
    width: 14px;
    height: 14px;
    flex: none;
  }
  .contact .indent { padding-left: 24px; }
  .brand {
    position: absolute;
    left: 560px;
    top: 230px;
    width: 380px;
    display: flex;
    align-items: center;
    gap: 16px;
  }
  .brand-dot {
    width: 34px;
    height: 34px;
    border-radius: 50%;
    background: var(--brand-maroon);
    flex: none;
  }
  .brand-name {
    font-size: 34px;
    font-weight: 600;
    color: var(--brand-maroon);
    letter-spacing: 0.06em;
    line-height: 1.1;
    text-transform: uppercase;
  }
</style>
</head>
<body>
  <div class="card">
    <svg class="card-art" width="1000" height="571" viewBox="0 0 1000 571" aria-hidden="true">
      <defs>
        <linearGradient id="swoosh" x1="0" y1="0" x2="1" y2="0">
          <stop offset="0" stop-color="#8c8c8c"/>
          <stop offset="1" stop-color="#d9d9d9"/>
        </linearGradient>
      </defs>
      <path class="swoosh-band" fill="url(#swoosh)"
            d="M600,0 H650 C545,130 478,320 470,571 H420 C430,300 500,120 600,0 Z"/>
      <path class="maroon-panel" fill="#8e2b31"
            d="M0,0 H600 C500,120 430,300 420,571 H0 Z"/>
    </svg>

    <div class="holder">
      <p class="holder-name">Marcus D. Alvord</p>
      <p class="holder-title">President / Owner</p>
    </div>

    <ul class="contact">
      <li>
        <svg class="contact-icon" viewBox="0 0 14 14"><circle cx="7" cy="7" r="7" fill="#fff"/><path d="M7 3.2a2.4 2.4 0 0 0-2.4 2.4C4.6 7.5 7 10.8 7 10.8s2.4-3.3 2.4-5.2A2.4 2.4 0 0 0 7 3.2z" fill="#8e2b31"/></svg>
        712 Tamber Rd.
      </li>
      <li class="indent">Brennick, WI 54000</li>
      <li>
        <svg class="contact-icon" viewBox="0 0 14 14"><circle cx="7" cy="7" r="7" fill="#fff"/><path d="M4.6 3.6l1.3-.2.7 1.7-.8.6a5 5 0 0 0 2.5 2.5l.6-.8 1.7.7-.2 1.3C7.8 10 4 6.2 4.6 3.6z" fill="#8e2b31"/></svg>
        715.555.0148
      </li>
      <li>
        <svg class="contact-icon" viewBox="0 0 14 14"><circle cx="7" cy="7" r="7" fill="#fff"/><rect x="3.5" y="4.5" width="7" height="5" fill="none" stroke="#8e2b31" stroke-width="1"/><path d="M3.5 4.5L7 7.3l3.5-2.8" fill="none" stroke="#8e2b31" stroke-width="1"/></svg>
        malvord@lumorafinishworks.com
      </li>
      <li>
        <svg class="contact-icon" viewBox="0 0 14 14"><circle cx="7" cy="7" r="7" fill="#fff"/><circle cx="7" cy="7" r="3.6" fill="none" stroke="#8e2b31" stroke-width="1"/><path d="M3.4 7h7.2M7 3.4v7.2" stroke="#8e2b31" stroke-width="1"/></svg>
        www.lumorafinishworks.com
      </li>
    </ul>

    <div class="brand">
      <span class="brand-dot"></span>
      <span class="brand-name">Lumora<br>Finish Works</span>
    </div>
  </div>
</body>
</html>
```